Brochure for High Net Worth Financial Advisory business

I would like to get a brochure designed that has the first few pages discussing our philosophy and process for investing.
We believe that model portfolios that are directly owned by clients and then monitored by our portfolio team are a solution to the opaqueness of managed funds and by then layering protection strategies over the top of these portfolios clients can get a better risk reward outcome.
The brochure would need to include a sleeve at the back in which we can place our paper portfolio documents and a slot for a business card would be appreciated.
We would like to convey strength, security and innovation in finance with our target market being high net worth individuals ($2m+) and other financial institutions.
Target Market(s)
High net worth investing clients, financial institutions
Industry/Entity Type
Financial
Requirements
Must have
- The text that included - diagrams if they suit
A sleeve for A4 paper
A holder for business cards
Nice to have
- Out logo is on the first page, with our catch line, it would be nice to incorporate this within the document

```html
<!DOCTYPE html>
<html lang="en">
<head>
<meta charset="utf-8">
<title>Harbourline Wealth Partners – Brochure</title>
<link href="https://fonts.googleapis.com/css2?family=Arimo:wght@400;700&display=swap" rel="stylesheet">
<style>
  :root{
    --stage:#d6d6d6;
    --ink:#1b1b1b;
    --white:#ffffff;
    --teal:#1f9cc0;
    --teal-light:#7fd0e6;
    --charcoal:#222222;
    --steel:#bdbdbd;
    --brand:#5f97b0;
    --navy:#1d3550;
    --box:#8fc3dc;
    --caption:#222222;
  }
  *{box-sizing:border-box;margin:0;padding:0}
  html,body{width:1200px;height:880px;overflow:hidden}
  body{background:var(--stage);font-family:"Arimo",Arial,sans-serif;color:var(--ink);position:relative}

  .panel{position:absolute;overflow:hidden;background:var(--white)}
  .panel svg.panel-art{position:absolute;inset:0;width:100%;height:100%}

  .cover{left:84px;top:143px;width:516px;height:355px}
  .spread{left:620px;top:110px;width:516px;height:355px}
  .card-holder{left:545px;top:555px;width:360px;height:252px}

  .brand-name{position:absolute;font-family:"Arimo",Arial,sans-serif;font-weight:400;
    color:var(--brand);text-transform:uppercase;letter-spacing:.06em;white-space:nowrap}
  .cover .brand-name{left:0;right:0;top:64px;text-align:center;font-size:24px}
  .spread .brand-name{right:14px;top:22px;font-size:11px}
  .card-holder .brand-name.holder-mark{left:22px;top:118px;font-size:17px}

  .hero-image{position:absolute;left:0;top:100px;width:516px;height:150px;
    background:linear-gradient(180deg,#c9d6ee 0%,#7f95c4 45%,#a9bde0 75%,#dfe7f4 100%)}

  .tagline{position:absolute;color:var(--white);font-size:11.5px;line-height:1.2;text-align:center}
  .cover .tagline{left:150px;width:220px;top:256px}
  .spread .tagline{left:6px;top:314px;width:220px;font-size:7px;text-align:left;transform:rotate(-5deg);transform-origin:left top}

  .web{position:absolute;color:var(--white);font-size:9px}
  .cover .web{right:18px;bottom:14px}
  .spread .web{right:18px;bottom:12px}

  .service-diagram{position:absolute;left:10px;top:55px;width:230px;height:230px}
  .service-copy{position:absolute;left:262px;top:56px;width:210px}
  .service-copy h2{font-size:12.5px;font-weight:700;margin-bottom:8px;margin-left:10px}
  .service-copy ul{list-style:disc;padding-left:28px;font-size:10.5px;line-height:1.22}
  .service-copy li{margin-bottom:1px}

  .card{position:absolute;border-radius:8px}
  .card-back{left:232px;top:95px;width:112px;height:112px;background:linear-gradient(135deg,#b9dcee,#6fb4d8)}
  .card-back .brand-name{left:54px;top:8px;font-size:7px;transform:rotate(90deg);transform-origin:left top}
  .card-front{left:228px;top:170px;width:120px;height:74px;background:linear-gradient(135deg,#f0f0f0,#c8c8c8)}
  .card-front .brand-name{left:0;right:0;top:30px;text-align:center;font-size:7px}

  .caption{position:absolute;font-size:12px;color:var(--caption)}
  .caption-cover{left:309px;top:517px}
  .caption-holder{left:672px;top:829px}
</style>
</head>
<body>

<section class="panel cover" aria-label="Brochure cover">
  <svg class="panel-art" viewBox="0 0 516 355" preserveAspectRatio="none" aria-hidden="true">
    <defs>
      <linearGradient id="coverSteel" x1="0" x2="1" y1="0" y2="0">
        <stop offset="0" stop-color="#1a1a1a"/><stop offset=".55" stop-color="#cfcfcf"/><stop offset="1" stop-color="#1e1e1e"/>
      </linearGradient>
    </defs>
    <rect width="516" height="355" fill="url(#coverSteel)"/>
    <path d="M60,0 C200,5 360,0 516,0 L516,100 L0,100 L0,70 C20,30 40,10 60,0Z" fill="var(--white)"/>
    <path d="M0,40 C60,10 140,0 200,0 L150,0 C90,5 40,20 0,55Z" fill="var(--teal)"/>
    <rect x="0" y="92" width="516" height="8" fill="var(--teal)"/>
    <path d="M0,250 C120,260 240,250 320,250 L0,250 L0,262 C80,262 200,256 320,250Z" fill="#e8e8e8"/>
    <path d="M0,285 C150,320 330,335 516,305 L516,330 C330,355 150,345 0,305Z" fill="var(--teal)"/>
    <path d="M0,278 C150,312 330,327 516,298 L516,302 C330,331 150,318 0,283Z" fill="var(--teal-light)"/>
  </svg>
  <span class="brand-name">Harbourline Wealth Partners</span>
  <div class="hero-image" role="img" aria-label="Photograph of a long, bright moving walkway in a modern terminal"></div>
  <p class="tagline">“Providing comprehensive, innovative and pro-active research, advice, and investment management services”</p>
  <span class="web">harbourlinegroup.com</span>
</section>

<section class="panel spread" aria-label="Servicing our clients page">
  <svg class="panel-art" viewBox="0 0 516 355" preserveAspectRatio="none" aria-hidden="true">
    <defs>
      <linearGradient id="spreadSteel" x1="0" x2="1"><stop offset="0" stop-color="#9a9a9a"/><stop offset="1" stop-color="#151515"/></linearGradient>
    </defs>
    <path d="M0,0 L140,0 C80,5 30,25 0,50Z" fill="#1b1b1b"/>
    <path d="M0,55 C40,25 120,5 220,0 L160,0 C90,8 40,25 0,42Z" fill="var(--teal)"/>
    <path d="M0,300 C150,330 330,320 516,280 L516,355 L0,355Z" fill="url(#spreadSteel)"/>
    <path d="M0,300 C150,330 330,320 516,280 L516,292 C330,330 150,345 0,335Z" fill="var(--teal)"/>
  </svg>
  <span class="brand-name">Harbourline Wealth Partners</span>

  <svg class="service-diagram" viewBox="0 0 230 230" aria-label="Client service model diagram">
    <g fill="none" stroke="#7fb3cf" stroke-width="1">
      <circle cx="115" cy="115" r="100"/><circle cx="115" cy="115" r="64"/>
    </g>
    <circle cx="115" cy="107" r="22" fill="var(--navy)"/>
    <text x="115" y="102" font-size="5" fill="#fff" text-anchor="middle" font-family="Arimo, sans-serif">Client</text>
    <text x="115" y="108" font-size="5" fill="#fff" text-anchor="middle" font-family="Arimo, sans-serif">Model</text>
    <text x="115" y="114" font-size="5" fill="#fff" text-anchor="middle" font-family="Arimo, sans-serif">Portfolio</text>
    <g font-family="Arimo, sans-serif" font-size="4.5" fill="#1d3550" text-anchor="middle">
      <rect x="97" y="74" width="36" height="11" fill="var(--box)"/><text x="115" y="81">Adviser</text>
      <rect x="97" y="130" width="36" height="13" fill="var(--navy)"/><text x="115" y="138" fill="#fff">Investment Mgmt</text>
      <rect x="140" y="70" width="36" height="12" fill="var(--box)"/><text x="158" y="78">Aust. Equities</text>
      <rect x="150" y="105" width="36" height="12" fill="var(--box)"/><text x="168" y="113">Intl. Equities</text>
      <rect x="140" y="143" width="36" height="11" fill="var(--box)"/><text x="158" y="150">Risk Mgmt</text>
      <rect x="100" y="162" width="32" height="11" fill="var(--box)"/><text x="116" y="169">Property</text>
      <rect x="58" y="150" width="26" height="11" fill="var(--box)"/><text x="71" y="157">Cash</text>
      <rect x="48" y="108" width="34" height="12" fill="var(--box)"/><text x="65" y="116">Alternatives</text>
      <rect x="58" y="72" width="34" height="11" fill="var(--box)"/><text x="75" y="79">Fixed Income</text>
      <rect x="98" y="14" width="34" height="11" fill="var(--box)"/><text x="115" y="21">Compliance</text>
      <rect x="190" y="108" width="34" height="11" fill="var(--box)"/><text x="207" y="115">Operations</text>
      <rect x="98" y="206" width="34" height="11" fill="var(--box)"/><text x="115" y="213">Reporting</text>
      <rect x="4" y="98" width="34" height="11" fill="var(--box)"/><text x="21" y="105">Governance</text>
    </g>
  </svg>

  <div class="service-copy">
    <h2>Servicing our clients</h2>
    <ul>
      <li>Our clients are central to our organisation.</li>
      <li>We orbit our clients to provide them with the appropriate levels of support and information.</li>
      <li>Every client is assigned a client relationship manager who is available for clients to discuss any aspect of their portfolio or engagement with HWP.</li>
      <li>They will then organise the most appropriate expert within the organisation to help them with their needs.</li>
    </ul>
  </div>
  <p class="tagline">“Providing comprehensive, innovative and pro-active research, advice, and investment management services”</p>
  <span class="web">harbourlinegroup.com</span>
</section>

<section class="panel card-holder" aria-label="Business card holder">
  <svg class="panel-art" viewBox="0 0 360 252" preserveAspectRatio="none" aria-hidden="true">
    <defs>
      <linearGradient id="holderSteel" x1="0" x2="1"><stop offset="0" stop-color="#1a1a1a"/><stop offset=".6" stop-color="#c8c8c8"/><stop offset="1" stop-color="#1e1e1e"/></linearGradient>
    </defs>
    <rect width="360" height="252" fill="url(#holderSteel)"/>
    <path d="M0,75 C90,25 220,10 360,12 L360,220 C250,210 120,215 0,210Z" fill="var(--white)"/>
    <path d="M0,75 C90,25 220,10 360,12 L360,4 C220,2 90,15 0,60Z" fill="var(--teal)"/>
    <path d="M0,205 C120,212 250,208 360,225 L360,238 C250,222 120,226 0,230Z" fill="var(--teal)"/>
  </svg>
  <span class="brand-name holder-mark">Harbourline Wealth Partners</span>
  <div class="card card-back"><span class="brand-name">Harbourline Wealth Partners</span></div>
  <div class="card card-front"><span class="brand-name">Harbourline Wealth Partners</span></div>
</section>

<p class="caption caption-cover">Cover Page</p>
<p class="caption caption-holder">Business card holder</p>

</body>
</html>
```